Car finance company business card

Create a nice business card for our car financing company , Visit our website www.birchlanefinance.com for the phone number and idea of the company look. Please do not be afraid to be creative. Name on card Is Marc-Antoine Beaulieu and phone number is on our website adress of business is
27816 Boulevard Saint-Orvel,
Mirabel, QC K4R 2T8

```html
<!DOCTYPE html>
<html lang="en">
<head>
<meta charset="utf-8">
<title>Birch Lane Finance – Business Card</title>
<link rel="stylesheet" href="https://fonts.googleapis.com/css2?family=Poppins:wght@400;600;800&display=swap">
<style>
  :root {
    --bg: #2b2e33;
    --orange: #f26a1b;
    --orange-light: #f7892f;
    --white: #ffffff;
    --ink: #1c1c1c;
    --text-dark: #2a1a10;
  }
  * { margin: 0; padding: 0; box-sizing: border-box; }
  html, body { width: 1200px; height: 900px; overflow: hidden; }
  body {
    background: var(--bg);
    font-family: "Poppins", sans-serif;
    position: relative;
  }
  .card {
    position: absolute;
    top: 300px;
    width: 525px;
    height: 300px;
    border-radius: 22px;
    overflow: hidden;
  }
  .card--front { left: 50px; background: var(--orange); }
  .card--back {
    left: 625px;
    background: linear-gradient(135deg, var(--orange-light), var(--orange));
  }
  .card__wave { position: absolute; inset: 0; width: 100%; height: 100%; }
  .contact {
    position: absolute;
    left: 30px;
    top: 34px;
    color: var(--text-dark);
  }
  .contact__name { font-size: 17px; font-weight: 600; line-height: 1.2; }
  .contact__title { font-size: 11px; font-weight: 400; margin-bottom: 12px; }
  .contact__row {
    display: flex; align-items: center; gap: 8px;
    font-size: 12px; margin-bottom: 6px;
  }
  .contact__row svg { width: 13px; height: 13px; flex: none; }
  .address {
    position: absolute;
    right: 28px;
    bottom: 20px;
    text-align: right;
    font-size: 13px;
    line-height: 1.5;
    color: var(--text-dark);
  }
  .brand {
    position: absolute;
    display: flex;
    align-items: center;
    gap: 8px;
    font-weight: 800;
    color: var(--ink);
    line-height: 1;
    white-space: nowrap;
  }
  .brand__dot { border-radius: 50%; background: var(--ink); flex: none; }
  .card--front .brand { left: 268px; top: 66px; font-size: 20px; }
  .card--front .brand__dot { width: 12px; height: 12px; }
  .card--back .brand { left: 40px; top: 70px; font-size: 36px; }
  .card--back .brand__dot { width: 20px; height: 20px; }
  .mascot {
    position: absolute;
    border-radius: 14px;
    background: linear-gradient(160deg, #f59a4a, #e0601a 60%, #5a63b8);
  }
  .card--front .mascot { left: 400px; top: 100px; width: 90px; height: 98px; }
  .card--back .mascot { left: 330px; top: 120px; width: 150px; height: 160px; }
</style>
</head>
<body>
  <section class="card card--front" aria-label="Business card front">
    <svg class="card__wave" viewBox="0 0 525 300" aria-hidden="true">
      <path d="M205 -5 C320 40 225 120 240 160 L215 175 L250 180 C300 215 420 215 535 195 L535 -5 Z"
            fill="var(--white)" stroke="var(--ink)" stroke-width="3"/>
    </svg>
    <div class="contact">
      <p class="contact__name">Marc-Antoine Beaulieu</p>
      <p class="contact__title">Director</p>
      <p class="contact__row">
        <svg viewBox="0 0 24 24"><path fill="var(--text-dark)" d="M6.6 10.8a15 15 0 0 0 6.6 6.6l2.2-2.2a1 1 0 0 1 1-.25 11.4 11.4 0 0 0 3.6.6 1 1 0 0 1 1 1V20a1 1 0 0 1-1 1A17 17 0 0 1 3 4a1 1 0 0 1 1-1h3.5a1 1 0 0 1 1 1c0 1.25.2 2.45.6 3.6a1 1 0 0 1-.25 1z"/></svg>
        (450) 555-0187
      </p>
      <p class="contact__row">
        <svg viewBox="0 0 24 24"><circle cx="12" cy="12" r="10" fill="none" stroke="var(--text-dark)" stroke-width="2"/><path d="M2 12h20M12 2c3 3 3 17 0 20M12 2c-3 3-3 17 0 20" fill="none" stroke="var(--text-dark)" stroke-width="1.6"/></svg>
        www.birchlanefinance.com
      </p>
    </div>
    <div class="brand"><span class="brand__dot"></span>Birch Lane Finance</div>
    <div class="mascot" role="img" aria-label="Cartoon mascot character holding car keys"></div>
    <p class="address">27816 Boulevard Saint-Orvel,<br>Mirabel, QC K4R 2T8</p>
  </section>

  <section class="card card--back" aria-label="Business card back">
    <div class="brand"><span class="brand__dot"></span>Birch Lane Finance</div>
    <div class="mascot" role="img" aria-label="Cartoon mascot character holding car keys"></div>
  </section>
</body>
</html>
```